We are looking for a new website design for our SEO WEB Development Company. The URL is www.brellowcreativeworks.com

We want it to be a more powerful representation of what we do. We are also looking for a number of designers that we will give continuous business to every month. The persons design we choose will also get a proposal to complete 4 - 6 new designs for us every month for our clients.

Be creative as you can in your design submissions. We really want to stand out!

Just to give you an idea of what we like look at this site: http://www.tovandigitalstudio.com/

```html
<!DOCTYPE html>
<html lang="en">
<head>
<meta charset="utf-8">
<title>Brellow Interactive Group – Media Marketing Experts</title>
<link href="https://fonts.googleapis.com/css2?family=Arimo:ital,wght@0,400;0,700;1,400&family=PT+Serif:ital,wght@0,700;1,400&display=swap" rel="stylesheet">
<style>
:root{
  --orange:#e8731b;
  --orange-dark:#b8560c;
  --brown:#9a4e12;
  --ink:#2b2b2b;
  --text:#444;
  --muted:#6b6b6b;
  --gray-light:#f1f1f1;
  --gray:#d6d6d6;
  --gray-mid:#c4c4c4;
  --gray-dark:#9c9c9c;
  --white:#fff;
}
*{margin:0;padding:0;box-sizing:border-box}
html,body{width:738px;height:1200px;overflow:hidden;background:var(--white)}
body{font-family:"Arimo",Arial,sans-serif;color:var(--text);position:relative}
.abs{position:absolute}

/* header */
.site-header{left:0;top:0;width:738px;height:92px;background:linear-gradient(#fafafa,#d9d9d9)}
.brand{left:127px;top:26px;color:var(--brown);font-weight:700;line-height:1}
.brand-name{font-size:34px;letter-spacing:-1px}
.brand-sub{font-size:11px;letter-spacing:1.4px;margin-top:3px}
.tagline{right:103px;top:54px;color:var(--orange-dark);font-weight:700;font-size:14px}
.phone{right:103px;top:71px;font-weight:700;font-size:11.5px;color:var(--ink);display:flex;align-items:center;gap:5px}
.phone-icon{width:15px;height:15px;background:#555;border-radius:3px;display:flex;align-items:center;justify-content:center}

/* nav */
.main-nav{left:0;top:92px;width:738px;height:28px;background:linear-gradient(#e9e9e9,#c9c9c9);border-top:1px solid #f8f8f8;border-bottom:1px solid #b0b0b0}
.nav-item{top:7px;font-size:8.5px;font-weight:700;color:var(--orange-dark)}
.nav-item.active{top:4px;padding:3px 7px;border-radius:10px;background:linear-gradient(#fff,#dcdcdc);border:1px solid #c8c8c8}
.nav-brand{left:562px;top:7px;font-size:9px;font-weight:700;color:var(--brown)}

/* hero */
.hero{left:0;top:120px;width:738px;height:232px;background:radial-gradient(circle at 76% 22%,#ffd9a8 0,#f29a3d 12%,#d8741f 32%,#c0600f 70%,#a9520b 100%);overflow:hidden}
.hero h1{left:120px;top:57px;font-size:22px;color:var(--white);font-weight:700}
.hero h2{left:122px;top:88px;font-size:14.5px;color:var(--white);font-weight:700}
.hero p{left:122px;top:117px;width:230px;font-size:8.3px;line-height:13px;color:#fff3e3;font-weight:700}
.hero-chart{left:300px;top:30px}

/* services strip */
.service-strip{left:0;top:352px;width:738px;height:178px;background:#cfcfcf}
.card{top:6px;width:107px;height:163px;background:#e4e4e4;border:1px solid #bdbdbd;border-radius:3px;overflow:hidden}
.card-head{height:50px;background:linear-gradient(#fdfdfd,#dadada);border-bottom:1px solid #c5c5c5;padding:6px 4px 0 33px;font-size:8.3px;font-weight:700;color:#3a3a3a;line-height:10px;position:relative}
.card-icon{position:absolute;left:8px;top:8px;width:17px;height:17px;border-radius:50%}
.card-body{padding:5px 5px;font-size:7px;line-height:9.6px;color:#333;height:88px}
.btn-learn{margin-left:4px;display:inline-flex;align-items:center;gap:6px;height:18px;padding:0 4px 0 9px;font-size:7.8px;font-weight:700;color:#444;background:linear-gradient(#f4f4f4,#cdcdcd);border:1px solid #ababab;border-radius:3px}
.btn-learn .arr{width:10px;height:10px;background:#bbb;border:1px solid #999;font-size:6px;line-height:8px;text-align:center;color:#fff}
.card:first-child .btn-learn{background:linear-gradient(#bdbdbd,#9d9d9d)}

/* quote form */
.quote-box{left:92px;top:538px;width:553px;height:179px;border:1px solid #bcbcbc;background:var(--white)}
.quote-title{height:32px;background:linear-gradient(#f4f4f4,#d2d2d2);border-bottom:1px solid #bcbcbc;padding:8px 9px;font-size:14.5px;font-weight:700;color:#3a3a3a}
.step-num{font-size:78px;font-weight:700;color:#e9e9e9;line-height:1}
.field-label{left:16px;font-size:7.5px;font-weight:700;color:#333}
.field{left:10px;width:170px;height:18px;border-radius:4px;background:linear-gradient(#ececec,#f7f7f7);border:1px solid #d0d0d0}
.quote-copy{left:197px;top:46px;width:350px;font-size:7px;line-height:9.7px;color:#444}
.btn-submit{left:196px;top:136px;width:173px;height:19px;border-radius:4px;background:linear-gradient(#fbfbfb,#d6d6d6);border:1px solid #b7b7b7;font-size:8.5px;font-weight:700;color:#333;text-align:center;line-height:17px}
.call-line{left:381px;top:141px;font-size:8.5px;font-weight:700;color:#333}

/* section headings */
.sec-head{font-size:17px;color:var(--ink);letter-spacing:-.4px}
.sec-head b{color:var(--orange);font-weight:400}
.sec-rule{height:3px;background:var(--orange);border-bottom:2px solid #d9d9d9}

/* blog */
.blog-list{left:92px;top:756px;width:171px;list-style:none}
.blog-list li{position:relative;padding:4px 6px 5px 13px;font-size:7.8px;font-weight:700;color:#333;line-height:10px;border-bottom:1px dashed #c8c8c8}
.blog-list li:first-child{background:#e6e6e6}
.blog-list li::before{content:"";position:absolute;left:3px;top:6px;width:5px;height:3px;background:var(--orange)}
.blog-link{left:92px;top:894px;width:171px;height:20px;background:#d0d0d0;border-top:3px solid var(--orange);font-size:7.8px;color:#333;padding:3px 0 0 14px}
.divider{left:271px;top:730px;width:0;height:186px;border-left:1px dotted #b8b8b8}

.about-copy{left:289px;top:756px;width:356px;font-size:7px;line-height:9.6px;color:#555}
.about-copy em{color:var(--orange);font-style:italic}
.testimonial{top:824px;width:165px;font-family:"PT Serif",Georgia,serif;font-style:italic;font-size:7.8px;line-height:10px;color:#333;padding-left:24px;position:absolute}
.testimonial::before{content:"\201C";position:absolute;left:0;top:-6px;font-size:34px;color:#c9c9c9;font-style:normal}
.cite{text-align:right;margin-top:5px;font-style:normal}
.cite strong{display:block;font-weight:700;font-size:7.8px}
.cite span{font-style:italic;font-size:7.5px}

/* services offered */
.promo-photo{left:205px;top:978px;width:158px;height:73px;border-radius:4px;background:linear-gradient(90deg,#f3f3f3,#e2e2e2 40%,#f0f0f0)}
.promo-line{left:98px;top:1008px;font-size:7.5px;letter-spacing:.5px;color:#666;line-height:9px}
.promo-line span{color:var(--orange)}
.promo-call{left:150px;top:1066px;font-size:8.5px;font-weight:700;color:#333}
.svc-col h4{font-size:8.3px;font-weight:700;color:var(--orange);margin-bottom:3px;line-height:10px}
.svc-col ul{list-style:none;margin-bottom:8px}
.svc-col li{font-size:7.3px;color:#222;line-height:10px;font-weight:700;padding-left:6px;position:relative}
.svc-col li::before{content:"›";position:absolute;left:0;top:0}

/* partners */
.partners{left:0;top:1091px;width:738px;height:70px;background:#e6e6e6;border-top:1px solid #d2d2d2}
.partner{top:22px;font-size:26px;font-weight:700;color:#555;letter-spacing:-.5px}

/* footer */
.site-footer{left:0;top:1161px;width:738px;height:39px;background:#c6c6c6}
.copyright{left:97px;top:15px;font-size:8.3px;font-weight:700;color:#333}
.share{left:536px;top:15px;font-size:8.3px;font-weight:700;color:#333}
.share-box{left:621px;top:9px;width:19px;height:19px;background:#666;border-radius:2px}
</style>
</head>
<body>

<header class="site-header abs">
  <div class="brand abs">
    <div class="brand-name">Brellow</div>
    <div class="brand-sub">INTERACTIVE GROUP</div>
  </div>
  <div class="tagline abs">Media Marketing Experts</div>
  <div class="phone abs">
    <span class="phone-icon"><svg width="9" height="9" viewBox="0 0 10 10"><path d="M2 1l2 2-1 1.3c.6 1.2 1.5 2.1 2.7 2.7L7 6l2 2-1.3 1.3C4.5 9 1 5.5.7 2.3z" fill="#fff"/></svg></span>
    877-555-0142
  </div>
</header>

<nav class="main-nav abs">
  <span class="nav-item active abs" style="left:119px">Creative Design</span>
  <span class="nav-item abs" style="left:225px">Website Design</span>
  <span class="nav-item abs" style="left:329px">Internet Marketing</span>
  <span class="nav-item abs" style="left:441px">IT Consulting</span>
  <span class="nav-brand abs">Brellow</span>
</nav>

<section class="hero abs">
  <h1 class="abs">Focusing on your brand</h1>
  <h2 class="abs">With the right Internet Marketing Tools</h2>
  <p class="abs">Lorem Ipsum is simply dummy text of the printing and typesetting industry. Lorem Ipsum has been the industry's standard dummy text ever since the 1500s</p>
  <svg class="hero-chart abs" width="340" height="200" viewBox="0 0 340 200">
    <rect x="82" y="160" width="22" height="36" fill="#d11a1a"/>
    <rect x="110" y="145" width="24" height="51" fill="#e8570f"/>
    <rect x="140" y="126" width="26" height="70" fill="#e6b812"/>
    <rect x="172" y="106" width="28" height="90" fill="#cfdc14"/>
    <rect x="206" y="86" width="30" height="110" fill="#7dd31c"/>
    <rect x="242" y="65" width="32" height="131" fill="#2fc02a"/>
    <polyline points="60,150 120,128 150,112 175,118 205,68 232,86 300,22" fill="none" stroke="#2d6fd4" stroke-width="6" stroke-linejoin="round"/>
    <polygon points="312,14 292,20 304,32" fill="#2d6fd4"/>
  </svg>
</section>

<section class="service-strip abs">
  <article class="card abs" style="left:93px">
    <div class="card-head"><span class="card-icon" style="background:#2d7fd6"></span>Brellow Interactive Group</div>
    <p class="card-body">is a leading Dallas Web Site Design, Publishing and Internet Marketing Firm. Our Dallas Texas based Website Design and Internet Marketing experts are some of the best in the industry!</p>
    <span class="btn-learn">Learn More <span class="arr">›</span></span>
  </article>
  <article class="card abs" style="left:204px">
    <div class="card-head"><span class="card-icon" style="background:#3a8fe0"></span>Brellow Interactive Web</div>
    <p class="card-body">is a full-service Dallas based Advertising Agency comprised of experienced advertising and marketing professionals that provide clients with a clear and distinct voice in the marketplace.</p>
    <span class="btn-learn">Learn More <span class="arr">›</span></span>
  </article>
  <article class="card abs" style="left:315px">
    <div class="card-head"><span class="card-icon" style="background:#7cb342;border-radius:2px"></span>Brellow Interactive Publishing</div>
    <p class="card-body">provides full-service custom publishing and consulting services for magazines, newsletters, blogs and web sites. We are the complete interactive publishing arm for your organization.</p>
    <span class="btn-learn">Learn More <span class="arr">›</span></span>
  </article>
  <article class="card abs" style="left:426px">
    <div class="card-head"><span class="card-icon" style="background:#4a78b8;border-radius:2px"></span>Brellow Interactive Media</div>
    <p class="card-body">provides cost-effective Web Site Design services, Search Engine Marketing, Internet Advertising, Internet Marketing Campaigns and most important, we can accommodate any budget.</p>
    <span class="btn-learn">Learn More <span class="arr">›</span></span>
  </article>
  <article class="card abs" style="left:537px">
    <div class="card-head"><span class="card-icon" style="background:#e0662a;border-radius:2px"></span>Brellow Interactive Reputation Management &amp; Repair</div>
    <p class="card-body">provides reputation management and repair services to the online community. We offer a plan of action to create a process of tracking an entity's actions and other entities' opinions about those actions;</p>
    <span class="btn-learn">Learn More <span class="arr">›</span></span>
  </article>
</section>

<section class="quote-box abs">
  <div class="quote-title">Get a Free Reputation Management &amp; Repair Quote!</div>
  <span class="step-num abs" style="left:2px;top:28px">1</span>
  <span class="step-num abs" style="left:190px;top:100px">2</span>
  <span class="field-label abs" style="top:43px">Name</span>
  <span class="field abs" style="top:52px"></span>
  <span class="field-label abs" style="top:72px">Phone Number</span>
  <span class="field abs" style="top:81px"></span>
  <span class="field-label abs" style="top:100px">Email</span>
  <span class="field abs" style="top:110px"></span>
  <span class="field-label abs" style="top:130px">Website Address</span>
  <span class="field abs" style="top:139px"></span>
  <p class="quote-copy abs">The goal of a reputation management or repair campaign is to create and/or strengthen an authoritative, positive image of your company by helping you gain positive name recognition across a wide range of websites. Most Search Engine users only pay attention to the Top 20 results, which is what we focus on. We will work closely with you to come up with a strong, detailed plan to put you at the top of search engins such as Searchly.com and above the negative listings about you. We will analyze your situation closely and create a detailed but flexible plan for your Reputation Management Campaign.</p>
  <span class="btn-submit abs">Submit Request for Quote</span>
  <span class="call-line abs">Or Call us today: 214-555-0187</span>
</section>

<h3 class="sec-head abs" style="left:104px;top:726px"><b>Latests</b> from blog</h3>
<div class="sec-rule abs" style="left:92px;top:747px;width:171px"></div>
<ul class="blog-list abs">
  <li>Lorem ipsum dolor sit amet, consectetur adipiscing elit.</li>
  <li>Mauris at turpis quis justo aliquam varius id ac mauris.</li>
  <li>Nulla nec nisl est, eu commodo dolor.</li>
  <li>Duis quis ipsum et nunc vulputate ultrices hendrerit non urna.</li>
  <li>Morbi sagittis scelerisque tellus, vitae scelerisque sapien gravida ac.</li>
</ul>
<div class="blog-link abs">Visit our Blog Page</div>
<div class="divider abs"></div>

<h3 class="sec-head abs" style="left:289px;top:726px"><b>Brellow</b> Interactive</h3>
<div class="sec-rule abs" style="left:278px;top:745px;width:367px"></div>
<p class="about-copy abs">We believe developing personal relationships with our clients is crucial to creating a successful marketing plan, and we pride ourselves in our ability to offer them the individual attention they deserve. The more we know about you and your business, the better we can help you reach your goals. <em>Learn more.</em></p>

<h3 class="sec-head abs" style="left:289px;top:790px"><b>Satisfied</b> Clients</h3>
<div class="sec-rule abs" style="left:278px;top:809px;width:367px"></div>
<blockquote class="testimonial" style="left:279px">It is a long established fact that a reader will be distracted by the readable content of a page when looking at its layout. The point of using Lorem Ipsum is that it has a more-or-less normal distribution of letters, as opposed to using 'Content here, content here', making it look like readable English.
  <div class="cite"><strong>Marcus Hale</strong><span>Orchard Labs</span></div>
</blockquote>
<blockquote class="testimonial" style="left:473px;width:170px">There are many variations of passages of Lorem Ipsum available, but the majority have suffered alteration in some form, by injected humour, or randomised words which don't look even slightly believable.
  <div class="cite"><strong>Dana Whitlow</strong><span>Northgrid</span></div>
</blockquote>

<h3 class="sec-head abs" style="left:104px;top:936px"><b>Services</b> Offered</h3>
<div class="sec-rule abs" style="left:92px;top:955px;width:553px"></div>
<div class="promo-photo abs" role="img" aria-label="Photo of a relaxed businesswoman with a laptop in an orange chair and a man lounging on a white sofa"></div>
<p class="promo-line abs">NOT ONLY <span>BRELLOW.</span><br>&nbsp;&nbsp;&nbsp;&nbsp;BUT <span>SOLUTIONS.</span></p>
<p class="promo-call abs">Call us for a quote today: 214-555-0187</p>

<div class="svc-col abs" style="left:372px;top:970px">
  <h4>Creative Design</h4>
  <ul><li>Creative Advertising</li><li>Print Design</li><li>Corporate Identity</li><li>Packaging</li></ul>
  <h4>Internet Marketing Services</h4>
  <ul><li>Search Engine Optimization</li><li>Pay-per-Click Campaign Consulting</li><li>Email Marketing</li><li>SEO Copywriting Reputation Management</li></ul>
</div>
<div class="svc-col abs" style="left:538px;top:970px">
  <h4>Website Design</h4>
  <ul><li>Web Design</li><li>E-commerce</li><li>Multimedia</li><li>Web Application Development</li></ul>
  <h4>IT Consulting<br>Brellow Interactive</h4>
  <ul><li>About Us</li><li>Our Work</li><li>Contact Us</li></ul>
</div>

<section class="partners abs">
  <span class="partner abs" style="left:105px">Searchly</span>
  <span class="partner abs" style="left:226px">Lookwise</span>
  <span class="partner abs" style="left:368px">Scoutr</span>
  <span class="partner abs" style="left:485px">Querio</span>
  <span class="partner abs" style="left:575px">Tallo</span>
</section>

<footer class="site-footer abs">
  <span class="copyright abs">Copyright © Brellow Interactive 2011. All rights reserved.</span>
  <span class="share abs">Share on Chatterly</span>
  <span class="share-box abs"></span>
</footer>

</body>
</html>
```